Business Cards and Stationery Set
Curavend Healthcare
Professional
Teodor Lisk, MD
Managing Partner
4318 West Birch Lane, Suite 207-3
Fresno, CA 93520 USA
tlisk@curavendcare.example
www.curavendcare.example

```html
<!DOCTYPE html>
<html lang="en">
<head>
<meta charset="utf-8">
<title>Curavend Healthcare – Stationery Set</title>
<link href="https://fonts.googleapis.com/css2?family=Open+Sans:wght@400;600;700&display=swap" rel="stylesheet">
<style>
  :root {
    --stage: #e9e7e4;
    --paper: #ffffff;
    --brand-red: #c4161c;
    --deep-red: #7d0b10;
    --ink: #1d1d1d;
    --band: #141414;
    --muted: #8a8a8a;
    --rule: #b9b9b9;
    --flap-grey: #cfcfcf;
  }
  * { box-sizing: border-box; margin: 0; padding: 0; }
  html, body { width: 1200px; height: 514px; overflow: hidden; }
  body {
    background: var(--stage);
    font-family: "Open Sans", Arial, sans-serif;
    color: var(--ink);
    position: relative;
  }
  .sheet {
    position: absolute;
    background: var(--paper);
    box-shadow: 0 2px 8px rgba(0,0,0,.18);
    overflow: hidden;
  }
  .letterhead { left: 127px; top: 30px; width: 240px; height: 450px; }
  .fax-sheet  { left: 403px; top: 30px; width: 240px; height: 450px; }

  .brand {
    position: absolute;
    left: 0; right: 0; top: 20px;
    text-align: center;
  }
  .brand-mark {
    display: block;
    width: 16px; height: 16px;
    margin: 0 auto 3px;
    border-radius: 50%;
    background: var(--brand-red);
  }
  .brand-name {
    display: block;
    font-weight: 700;
    font-size: 15px;
    line-height: 1;
    color: var(--brand-red);
    letter-spacing: -.2px;
  }
  .brand-tag {
    display: block;
    font-size: 4.5px;
    letter-spacing: 1.4px;
    text-transform: uppercase;
    color: var(--muted);
    margin-top: 2px;
  }
  .faint-disc {
    position: absolute;
    right: 14px; bottom: 62px;
    width: 40px; height: 40px;
    border-radius: 50%;
    background: var(--brand-red);
    opacity: .08;
  }
  .footer-band {
    position: absolute;
    left: 0; bottom: 0;
    width: 100%; height: 52px;
  }
  .footer-text {
    position: absolute;
    left: 22px; bottom: 10px;
    font-size: 4px;
    line-height: 6px;
    color: #e2e2e2;
  }
  .footer-web {
    position: absolute;
    right: 18px; bottom: 10px;
    font-size: 4px;
    line-height: 6px;
    color: #e2e2e2;
    text-align: right;
  }

  .fax-title {
    position: absolute;
    left: 24px; top: 82px;
    font-size: 17px;
    font-weight: 400;
    letter-spacing: .5px;
  }
  .fax-fields {
    position: absolute;
    left: 24px; top: 110px;
    width: 192px;
    display: grid;
    grid-template-columns: 1fr 1fr;
    column-gap: 14px;
    row-gap: 9px;
  }
  .fax-field {
    display: flex;
    align-items: flex-end;
    font-size: 4px;
    color: #444;
    border-bottom: .6px solid var(--rule);
    height: 8px;
  }
  .fax-checks {
    position: absolute;
    left: 24px; top: 178px;
    width: 192px;
    display: flex;
    justify-content: space-between;
    font-size: 3.8px;
    color: #444;
  }
  .check { display: flex; align-items: center; gap: 2px; }
  .check-box { width: 5px; height: 5px; border: .6px solid #777; }

  .envelope {
    position: absolute;
    width: 346px; height: 160px;
    background: var(--paper);
    box-shadow: 0 2px 8px rgba(0,0,0,.18);
    overflow: hidden;
  }
  .envelope-back  { left: 722px; top: 30px; }
  .envelope-front { left: 706px; top: 150px; height: 168px; }
  .envelope svg.flap { position: absolute; left: 0; top: 0; width: 100%; height: 100%; }
  .envelope-back .brand { top: 60px; }
  .envelope-front .brand { top: 52px; left: 18px; right: auto; text-align: left; }
  .envelope-front .brand-mark { margin: 0 0 3px; }
  .envelope-front .return-address {
    position: absolute; left: 18px; top: 96px;
    font-size: 4px; line-height: 6px; color: #555;
  }
  .envelope-front .footer-band { height: 34px; }
  .envelope-front .footer-web { bottom: 6px; }

  .card {
    position: absolute;
    width: 104px; height: 58px;
    border-radius: 3px;
    box-shadow: 0 2px 6px rgba(0,0,0,.2);
    overflow: hidden;
  }
  .card-front { left: 772px; top: 370px; background: var(--paper); }
  .card-back  {
    left: 886px; top: 370px;
    background: radial-gradient(circle at 30% 40%, var(--brand-red), var(--deep-red));
  }
  .card-front .brand { top: 8px; left: 8px; right: auto; text-align: left; }
  .card-front .brand-mark { width: 8px; height: 8px; margin: 0 0 2px; }
  .card-front .brand-name { font-size: 9px; }
  .card-front .brand-tag { font-size: 3px; letter-spacing: .8px; }
  .card-person {
    position: absolute; left: 8px; top: 33px;
    font-size: 3.6px; line-height: 4.8px;
  }
  .card-person strong { font-weight: 700; }
  .card-front .footer-band { height: 12px; }
  .card-back .back-disc {
    position: absolute; left: 40px; top: 17px;
    width: 24px; height: 24px; border-radius: 50%;
    background: rgba(255,255,255,.9);
  }
</style>
</head>
<body>

<section class="sheet letterhead" aria-label="Letterhead">
  <div class="brand">
    <span class="brand-mark"></span>
    <span class="brand-name">Curavend</span>
    <span class="brand-tag">Healthcare</span>
  </div>
  <div class="faint-disc"></div>
  <svg class="footer-band" viewBox="0 0 240 52" preserveAspectRatio="none">
    <path d="M0 14 Q120 34 240 10 L240 52 L0 52 Z" fill="var(--band)"/>
    <path d="M0 14 Q120 34 240 10" fill="none" stroke="var(--brand-red)" stroke-width="2"/>
    <path d="M0 20 Q130 38 240 16" fill="none" stroke="var(--deep-red)" stroke-width="1"/>
  </svg>
  <p class="footer-text">4318 West Birch Lane, Suite 207-3<br>Fresno, CA 93520 USA</p>
  <p class="footer-web">T +1 559 555 0142<br>www.curavendcare.example</p>
</section>

<section class="sheet fax-sheet" aria-label="Fax cover sheet">
  <div class="brand">
    <span class="brand-mark"></span>
    <span class="brand-name">Curavend</span>
    <span class="brand-tag">Healthcare</span>
  </div>
  <h1 class="fax-title">FAX</h1>
  <div class="fax-fields">
    <span class="fax-field">To:</span><span class="fax-field">From:</span>
    <span class="fax-field">Fax:</span><span class="fax-field">Pages:</span>
    <span class="fax-field">Phone:</span><span class="fax-field">Date:</span>
    <span class="fax-field">Re:</span><span class="fax-field">CC:</span>
  </div>
  <div class="fax-checks">
    <span class="check"><span class="check-box"></span>Urgent</span>
    <span class="check"><span class="check-box"></span>For Review</span>
    <span class="check"><span class="check-box"></span>Please Comment</span>
    <span class="check"><span class="check-box"></span>Please Reply</span>
    <span class="check"><span class="check-box"></span>Please Recycle</span>
  </div>
  <svg class="footer-band" viewBox="0 0 240 52" preserveAspectRatio="none">
    <path d="M0 14 Q120 34 240 10 L240 52 L0 52 Z" fill="var(--band)"/>
    <path d="M0 14 Q120 34 240 10" fill="none" stroke="var(--brand-red)" stroke-width="2"/>
    <path d="M0 20 Q130 38 240 16" fill="none" stroke="var(--deep-red)" stroke-width="1"/>
  </svg>
  <p class="footer-text">4318 West Birch Lane, Suite 207-3<br>Fresno, CA 93520 USA</p>
  <p class="footer-web">F +1 559 555 0143<br>www.curavendcare.example</p>
</section>

<section class="envelope envelope-back" aria-label="Envelope, back">
  <svg class="flap" viewBox="0 0 346 160" preserveAspectRatio="none">
    <defs>
      <linearGradient id="flapRed" x1="0" y1="0" x2="1" y2="0">
        <stop offset="0" stop-color="#e2262c"/>
        <stop offset="1" stop-color="#7d0b10"/>
      </linearGradient>
    </defs>
    <path d="M0 0 L346 0 L346 8 L173 58 L0 8 Z" fill="url(#flapRed)"/>
  </svg>
  <div class="brand">
    <span class="brand-mark"></span>
    <span class="brand-name">Curavend</span>
    <span class="brand-tag">Healthcare</span>
  </div>
</section>

<section class="envelope envelope-front" aria-label="Envelope, front">
  <svg class="flap" viewBox="0 0 346 168" preserveAspectRatio="none">
    <path d="M0 0 L346 0 L346 6 L173 44 L0 6 Z" fill="var(--flap-grey)"/>
  </svg>
  <div class="brand">
    <span class="brand-mark"></span>
    <span class="brand-name">Curavend</span>
    <span class="brand-tag">Healthcare</span>
  </div>
  <p class="return-address">4318 West Birch Lane, Suite 207-3<br>Fresno, CA 93520 USA</p>
  <svg class="footer-band" viewBox="0 0 346 34" preserveAspectRatio="none">
    <path d="M0 10 Q173 26 346 6 L346 34 L0 34 Z" fill="var(--band)"/>
    <path d="M0 10 Q173 26 346 6" fill="none" stroke="var(--brand-red)" stroke-width="2"/>
  </svg>
  <p class="footer-web">www.curavendcare.example</p>
</section>

<section class="card card-front" aria-label="Business card, front">
  <div class="brand">
    <span class="brand-mark"></span>
    <span class="brand-name">Curavend</span>
    <span class="brand-tag">Healthcare</span>
  </div>
  <p class="card-person"><strong>Teodor Lisk, MD</strong><br>Managing Partner<br>tlisk@curavendcare.example</p>
  <svg class="footer-band" viewBox="0 0 104 12" preserveAspectRatio="none">
    <path d="M0 4 Q52 10 104 2 L104 12 L0 12 Z" fill="var(--band)"/>
    <path d="M0 4 Q52 10 104 2" fill="none" stroke="var(--brand-red)" stroke-width="1"/>
  </svg>
</section>

<section class="card card-back" aria-label="Business card, back">
  <span class="back-disc"></span>
</section>

</body>
</html>
```